A colorful, playful, nerdy, creative logo for a business analytics and marketing analytics company.

We need a logo and website design for a new company based in Florida called Brightfold Pattern Works Collective. We provide marketing, consumer and business insights through the use of market research, business analytics and marketing analytics. We are a collection of several individuals each with specific expertise and come together to provide the best possible insights about their consumers/guests/customers. We would like to see a design that uses colors that show a free spirit but deeply rooted in analytics " a super nerd " Along those steps, we would like to see either a playful, nerdy, creative logo or one that includes the full or partial name of the company. We have simplified our "brand" by saying when you initially start with us you may have several questions "?" through the process of learning about your consumers/brand ">" incredible solutions, strategies are developed "!" So something like a ?>! symbol would be interesting. Although the name of the company sounds very complex and very long to write, we would be interested in thoughtful ways of shorting the name or incorporating into the final logo design

Target Market(s)

Business or organizations that currently do not have an analytics/research function

Industry/Entity Type

Business

Contact Information for Business Card

Incorporate final logo and colors font. In the past, I have used a "wordle" website to show 10 common research terms scattered about .. showing them as strength or core competencies.

Logo Text

?>! or Brightfold Pattern Works Collective or BPW Collective

Coding

Coded - Design and coding required

Number of Pages Required

4 page

Font styles to use
Sans Serif
Decorative

Requirements
Must have
• The project must communicate analytics/scientific. It must we unique but not unique for the sack of being unique.
• It must either be a logo or a simple way to communicate the company name Brightfold Pattern Works Collective
Nice to have
• Again incorporating the symbols ?>! in that order. Showing confusion to gaining insights and then developing incredible solutions that are used to effect consumer behavior.
• Look to CPG ( consumer package goods) industry to input
Should not have
• I am pretty open to suggestions.

```html
<!DOCTYPE html>
<html lang="en">
<head>
<meta charset="utf-8">
<title>BPW Collective — Business Insights</title>
<link href="https://fonts.googleapis.com/css2?family=Montserrat:wght@400;500;600;700&family=Open+Sans:wght@400;600&display=swap" rel="stylesheet">
<style>
:root{
  --dark:#262626;
  --dark-2:#2e2e2e;
  --blue:#1cb8ec;
  --blue-band:#00bdf2;
  --orange:#f07c24;
  --ink:#1c1c1c;
  --body:#555a60;
  --soft-bg:#f2f5f9;
  --card-border:#dfe3e8;
  --white:#ffffff;
}
*{box-sizing:border-box;margin:0;padding:0}
html,body{width:1200px;height:3163px;overflow:hidden}
body{font-family:"Open Sans",Arial,sans-serif;color:var(--body);background:var(--white);position:relative}
h1,h2,h3,h4,.nav,.btn,.brand{font-family:"Montserrat",Arial,sans-serif}
.section{position:absolute;left:0;width:1200px}

/* top bar */
.topbar{top:0;height:46px;background:var(--dark);color:#fff;font-size:13px}
.topbar .contact{position:absolute;left:88px;top:14px;display:flex;gap:30px}
.topbar .social{position:absolute;right:86px;top:12px;display:flex;gap:9px}
.dot-icon{width:20px;height:20px;border-radius:50%;background:#fff}

/* header */
.header{top:46px;height:118px;background:#fff}
.brand{position:absolute;left:86px;top:30px;display:flex;align-items:center;gap:14px;font-size:38px;font-weight:700;color:var(--blue);line-height:1}
.brand .dot{width:22px;height:22px;border-radius:50%;background:var(--orange)}
.nav{position:absolute;left:432px;top:52px;display:flex;font-size:13px;font-weight:500;color:var(--ink)}
.nav span{margin-right:28px}
.quote-btn{position:absolute;left:968px;top:38px;width:144px;height:43px;background:var(--blue);color:#fff;font-family:"Montserrat",sans-serif;font-size:14px;font-weight:500;display:flex;align-items:center;justify-content:center}

/* hero */
.hero{top:164px;height:429px;background:linear-gradient(135deg,#6b6058 0%,#8a7c6e 35%,#5d6670 70%,#3f3a36 100%)}
.hero-shade{position:absolute;inset:0;background:rgba(20,20,20,.35)}
.hero h1{position:absolute;top:150px;width:100%;text-align:center;color:#fff;font-size:36px;font-weight:700}
.hero p{position:absolute;top:208px;left:262px;width:676px;text-align:center;color:#fff;font-size:13.5px;line-height:22px}
.hero .btn{position:absolute;left:525px;top:285px;width:150px;height:51px;background:var(--blue);color:#fff;font-size:13px;display:flex;align-items:center;justify-content:center}
.arrow-box{position:absolute;top:186px;width:57px;height:57px;border:2px solid #fff;display:flex;align-items:center;justify-content:center;background:rgba(0,0,0,.2)}

/* services */
.services{top:593px;height:561px;background:var(--soft-bg)}
.section-title{position:absolute;width:100%;text-align:center;font-size:26px;font-weight:700;color:var(--ink);letter-spacing:.5px}
.lead{position:absolute;left:262px;width:676px;text-align:center;font-size:13px;line-height:22px}
.service-card{position:absolute;top:179px;width:323px;height:301px;background:#fff;border:1px solid var(--card-border);text-align:center}
.service-card svg{margin-top:36px}
.service-card .rule{width:72px;height:3px;background:var(--blue);margin:6px auto 0}
.service-card h3{margin-top:26px;font-size:17px;font-weight:600;color:var(--ink)}
.service-card.active h3{color:var(--blue)}
.service-card p{margin:12px auto 0;width:240px;font-size:12.5px;line-height:22px}

/* about */
.about{top:1154px;height:565px;background:#fff}
.about h2{position:absolute;left:86px;top:60px;font-size:26px;font-weight:700;color:var(--ink)}
.about .copy{position:absolute;left:86px;top:110px;width:580px;font-size:12.5px;line-height:22px}
.about .copy p+p{margin-top:18px}
.about .btn{position:absolute;left:86px;top:426px;width:152px;height:54px;background:var(--orange);color:#fff;font-size:13px;display:flex;align-items:center;justify-content:center}
.about-photo{position:absolute;left:723px;top:0;width:477px;height:565px;background:linear-gradient(160deg,#4a443d 0%,#8a8177 40%,#d8d4cf 65%,#6f6a64 100%)}

/* stats */
.stats{top:1719px;height:156px;background:var(--blue-band)}
.stat{position:absolute;top:17px;width:222px;height:124px;border:1.5px solid rgba(255,255,255,.85);color:#fff;text-align:center}
.stat strong{display:block;font-family:"Montserrat",sans-serif;font-size:48px;font-weight:500;margin-top:8px;line-height:58px}
.stat .line{width:172px;height:2px;background:#fff;margin:3px auto 8px}
.stat span{font-size:16px}

/* testimonials */
.testimonials{top:1875px;height:536px;background:var(--soft-bg)}
.testimonial{position:absolute;top:150px;width:323px;height:297px;background:#fff;border:1px solid var(--card-border)}
.avatar{position:absolute;left:30px;top:36px;width:76px;height:76px;border-radius:50%;border:2px solid #e3e7ec;background:radial-gradient(circle at 50% 40%,#b8a189,#6b5a4a)}
.testimonial h4{position:absolute;left:118px;top:52px;font-size:15px;font-weight:600;color:var(--ink)}
.testimonial .city{position:absolute;left:118px;top:76px;font-size:12.5px;color:var(--ink)}
.quote-mark{position:absolute;right:34px;top:28px;font-family:Georgia,serif;font-size:66px;font-weight:700;color:#b6e3f4;line-height:1}
.testimonial p{position:absolute;left:34px;top:138px;width:262px;font-size:12.5px;line-height:21px}
.pager{position:absolute;top:478px;left:567px;display:flex;gap:10px}
.pager i{width:15px;height:15px;border-radius:50%;border:2px solid #555;display:block}
.pager i.on{background:var(--blue);border-color:var(--blue)}

/* partners */
.partners{top:2411px;height:316px;background:#fff}
.partner{position:absolute;top:147px;width:242px;height:95px;border:2px solid #dcdcdc;display:flex;align-items:center;justify-content:center}
.partner div{background:#cfcfcf}

/* footer */
.footer{top:2727px;height:436px;background:var(--dark-2);color:#fff}
.footer .brand{left:86px;top:66px}
.footer h4{position:absolute;top:72px;font-size:20px;font-weight:500}
.f-contact{position:absolute;left:86px;top:133px;font-size:13.5px}
.f-contact div{display:flex;align-items:center;gap:14px;height:50px}
.f-social{position:absolute;left:86px;top:305px;display:flex;gap:20px}
.f-social i{width:30px;height:30px;border-radius:50%;border:1.5px solid #fff;display:block}
.links{position:absolute;left:472px;top:136px;font-size:13.5px}
.links div{display:flex;align-items:center;gap:18px;height:39px}
.news{position:absolute;left:736px;width:380px}
.news .thumb{position:absolute;left:0;top:0;width:70px;height:70px;background:linear-gradient(135deg,#c9cfd6,#7c8793)}
.news p{position:absolute;left:88px;top:-2px;width:290px;font-size:12.5px;line-height:21px;color:#c8a58a}
.news small{position:absolute;left:88px;top:50px;font-size:12px;color:#bdbdbd}
.footer .divider{position:absolute;left:86px;right:86px;top:384px;height:1px;background:#444}
.copyright{position:absolute;left:86px;top:401px;font-size:13px}
</style>
</head>
<body>

<header class="section topbar">
  <div class="contact"><span>Call: (555) 014-2730</span><span>Email: hello@bpwcollective.example</span></div>
  <div class="social"><i class="dot-icon"></i><i class="dot-icon"></i><i class="dot-icon"></i><i class="dot-icon"></i></div>
</header>

<nav class="section header">
  <div class="brand"><span class="dot"></span>BPWC</div>
  <div class="nav"><span>HOME</span><span>ABOUT US</span><span>SERVICES</span><span>CAREERS</span><span>BLOG</span><span>CONTACT US</span></div>
  <div class="quote-btn">GET A QUOTE</div>
</nav>

<section class="section hero" role="img" aria-label="Team of colleagues around a table reviewing printed charts and tablets">
  <div class="hero-shade"></div>
  <h1>We Help Businesses Innovate and grow</h1>
  <p>Lorem ipsum dolor sit amet, consectetuer adipiscing elit. Aenean commodo ligula eget dolor. Aenean massa. Cum sociis natoque penatibus et magnis dis parturient montes.</p>
  <div class="btn">VIEW MORE</div>
  <div class="arrow-box" style="left:0"><svg width="22" height="34" viewBox="0 0 22 34"><polyline points="18,2 4,17 18,32" fill="none" stroke="#fff" stroke-width="2.5"/></svg></div>
  <div class="arrow-box" style="right:0"><svg width="22" height="34" viewBox="0 0 22 34"><polyline points="4,2 18,17 4,32" fill="none" stroke="#fff" stroke-width="2.5"/></svg></div>
</section>

<section class="section services">
  <h2 class="section-title" style="top:64px">SERVICES WE OFFER</h2>
  <p class="lead" style="top:114px">Lorem ipsum dolor sit amet, consectetuer adipiscing elit. Aenean commodo ligula eget dolor. Aenean massa. Cum sociis natoque penatibus et magnis dis parturient montes, nascetur ridiculus mus.</p>

  <article class="service-card" style="left:86px">
    <svg width="80" height="74" viewBox="0 0 80 74"><rect x="4" y="36" width="12" height="34" fill="#8a8a8a"/><rect x="20" y="22" width="12" height="48" fill="#8a8a8a"/><rect x="36" y="6" width="12" height="30" fill="#8a8a8a"/><circle cx="48" cy="44" r="14" fill="none" stroke="#8a8a8a" stroke-width="5"/><line x1="58" y1="54" x2="74" y2="70" stroke="#8a8a8a" stroke-width="7"/></svg>
    <div class="rule"></div>
    <h3>MARKET RESEARCH</h3>
    <p>Lorem ipsum dolor sit amet, consectetuer adipiscing elit. Aenean commodo ligula eget dolor. Aenean</p>
  </article>
  <article class="service-card active" style="left:439px">
    <svg width="80" height="74" viewBox="0 0 80 74"><g stroke="#1cb8ec" stroke-width="3"><line x1="40" y1="2" x2="40" y2="10"/><line x1="12" y1="12" x2="18" y2="18"/><line x1="68" y1="12" x2="62" y2="18"/><line x1="4" y1="36" x2="12" y2="36"/><line x1="68" y1="36" x2="76" y2="36"/></g><circle cx="40" cy="36" r="18" fill="#1cb8ec"/><rect x="32" y="54" width="16" height="10" fill="#1cb8ec"/><text x="40" y="44" text-anchor="middle" font-family="Montserrat,sans-serif" font-size="22" font-weight="700" fill="#fff">$</text></svg>
    <div class="rule"></div>
    <h3>BUSINESS ANALYTICS</h3>
    <p>Lorem ipsum dolor sit amet, consectetuer adipiscing elit. Aenean commodo ligula eget dolor. Aenean</p>
  </article>
  <article class="service-card" style="left:789px">
    <svg width="80" height="74" viewBox="0 0 80 74"><g fill="none" stroke="#8a8a8a" stroke-width="3"><circle cx="40" cy="37" r="32"/><circle cx="40" cy="37" r="22"/><circle cx="40" cy="37" r="12"/></g><line x1="40" y1="37" x2="66" y2="64" stroke="#8a8a8a" stroke-width="4"/></svg>
    <div class="rule"></div>
    <h3>MARKETING ANALYTICS</h3>
    <p>Lorem ipsum dolor sit amet, consectetuer adipiscing elit. Aenean commodo ligula eget dolor. Aenean</p>
  </article>
</section>

<section class="section about">
  <h2>ABOUT BPWC</h2>
  <div class="copy">
    <p>Lorem ipsum dolor sit amet, consectetuer adipiscing elit. Aenean commodo ligula eget dolor. Aenean massa. Cum sociis natoque penatibus et magnis dis parturient montes, nascetur ridiculus mus. Donec quam felis, ultricies nec, pellentesque eu, pretium quis, sem. Nulla consequat massa quis enim. Donec pede justo, fringilla vel, aliquet nec, vulputate eget, arcu. In enim justo, rhoncus ut.</p>
    <p>Imperdiet a, venenatis vitae, justo. Nullam dictum felis eu pede mollis pretium. Integer tincidunt. Cras dapibus. Vivamus elementum semper nisi. Aenean vulputate eleifend tellus. Aenean leo ligula, porttitor eu, consequat vitae, eleifend ac, enim. Aliquam lorem ante, dapibus in, viverra quis, feugiat a, tellus. Phasellus viverra nulla ut metus varius laoreet. Quisque rutrum. Aenean imperdiet. Etiam ultricies nisi vel augue. Curabitur ullamcorper ultricies nisi. Nam eget dui. Etiam rhoncus.</p>
  </div>
  <div class="btn">KNOW MORE</div>
  <div class="about-photo" role="img" aria-label="Laptop showing a strategy slide on a desk with a coffee cup and papers"></div>
</section>

<section class="section stats">
  <div class="stat" style="left:86px"><strong>100+</strong><div class="line"></div><span>Sucessfull Projects</span></div>
  <div class="stat" style="left:354px"><strong>200+</strong><div class="line"></div><span>Happy Customers</span></div>
  <div class="stat" style="left:622px"><strong>10+</strong><div class="line"></div><span>Sucessfull Country</span></div>
  <div class="stat" style="left:890px"><strong>50+</strong><div class="line"></div><span>Ongoing Projects</span></div>
</section>

<section class="section testimonials">
  <h2 class="section-title" style="top:75px">TESTIMONIALS</h2>
  <article class="testimonial" style="left:86px">
    <div class="avatar" role="img" aria-label="Portrait of the client"></div>
    <h4>Marla Quinlan</h4><div class="city">Tampa</div><div class="quote-mark">”</div>
    <p>Lorem ipsum dolor sit amet, consectetuer adipiscing elit. Aenean commodo ligula eget dolor. Aenean massa. Cum sociis natoque penatibus et magnis dis parturient montes.</p>
  </article>
  <article class="testimonial" style="left:439px">
    <div class="avatar" role="img" aria-label="Portrait of the client"></div>
    <h4>Marla Quinlan</h4><div class="city">Tampa</div><div class="quote-mark">”</div>
    <p>Lorem ipsum dolor sit amet, consectetuer adipiscing elit. Aenean commodo ligula eget dolor. Aenean massa. Cum sociis natoque penatibus et magnis dis parturient montes.</p>
  </article>
  <article class="testimonial" style="left:789px">
    <div class="avatar" role="img" aria-label="Portrait of the client"></div>
    <h4>Marla Quinlan</h4><div class="city">Tampa</div><div class="quote-mark">”</div>
    <p>Lorem ipsum dolor sit amet, consectetuer adipiscing elit. Aenean commodo ligula eget dolor. Aenean massa. Cum sociis natoque penatibus et magnis dis parturient montes.</p>
  </article>
  <div class="pager"><i></i><i class="on"></i><i></i></div>
</section>

<section class="section partners">
  <h2 class="section-title" style="top:72px">OUR PARTNERS</h2>
  <div class="partner" style="left:93px"><div style="width:140px;height:30px;border-radius:15px"></div></div>
  <div class="partner" style="left:350px"><div style="width:44px;height:44px"></div></div>
  <div class="partner" style="left:610px"><div style="width:150px;height:22px"></div></div>
  <div class="partner" style="left:869px"><div style="width:120px;height:34px"></div></div>
</section>

<footer class="section footer">
  <div class="brand"><span class="dot"></span>BPWC</div>
  <div class="f-contact">
    <div><svg width="18" height="24" viewBox="0 0 18 24"><path d="M9 0C4 0 0 4 0 9c0 7 9 15 9 15s9-8 9-15c0-5-4-9-9-9z" fill="#fff"/><circle cx="9" cy="9" r="3.5" fill="#2e2e2e"/></svg>60 orem ipsum dolor sit amet, UK</div>
    <div><svg width="20" height="20" viewBox="0 0 20 20"><path d="M4 1l4 4-2 3c1 3 3 5 6 6l3-2 4 4-3 3C8 19 1 12 1 4z" fill="#fff"/></svg>(555) 014-2730</div>
    <div><svg width="22" height="16" viewBox="0 0 22 16"><rect width="22" height="16" fill="#fff"/><polyline points="0,0 11,9 22,0" fill="none" stroke="#2e2e2e" stroke-width="2"/></svg>hello@bpwcollective.example</div>
  </div>
  <div class="f-social"><i></i><i></i><i></i></div>

  <h4 style="left:465px">QUICK LINKS</h4>
  <div class="links">
    <div><svg width="14" height="12" viewBox="0 0 14 12"><path d="M0 6h12M7 1l5 5-5 5" fill="none" stroke="#fff" stroke-width="2"/></svg>About Us</div>
    <div><svg width="14" height="12" viewBox="0 0 14 12"><path d="M0 6h12M7 1l5 5-5 5" fill="none" stroke="#fff" stroke-width="2"/></svg>Services</div>
    <div><svg width="14" height="12" viewBox="0 0 14 12"><path d="M0 6h12M7 1l5 5-5 5" fill="none" stroke="#fff" stroke-width="2"/></svg>Careers</div>
    <div><svg width="14" height="12" viewBox="0 0 14 12"><path d="M0 6h12M7 1l5 5-5 5" fill="none" stroke="#fff" stroke-width="2"/></svg>Blog</div>
    <div><svg width="14" height="12" viewBox="0 0 14 12"><path d="M0 6h12M7 1l5 5-5 5" fill="none" stroke="#fff" stroke-width="2"/></svg>Contact Us</div>
  </div>

  <h4 style="left:736px">LATEST NEWS</h4>
  <div class="news" style="top:150px">
    <div class="thumb" role="img" aria-label="News thumbnail of documents on a desk"></div>
    <p>Lorem ipsum dolor sit amet, consectetuer adipiscing elit. Aenean commodo ligula</p>
    <small>Jan 05, 2017</small>
  </div>
  <div class="news" style="top:260px">
    <div class="thumb" role="img" aria-label="News thumbnail of documents on a desk"></div>
    <p>Lorem ipsum dolor sit amet, consectetuer adipiscing elit. Aenean commodo ligula</p>
    <small>Jan 05, 2017</small>
  </div>

  <div class="divider"></div>
  <div class="copyright">Copyright 2017 © BPWC All Rights Reserved.</div>
</footer>

</body>
</html>
```